Business Cards For A cell Phone Company
Linden Cellular
Business Cards For A cell Phone Company - Retailers
Creative Brief
Simple
Tobias Krell
Operations Manager
2864 Belmore Ave Cincinnati OH 45219
tobias.krell@lindencellular-mail.com
www.lindencellular-mail.com
Concepts
Business Cards/Letterhead/ Envelopes/Notepads/Tshirt/labels for quiet tin crate
Business cards and company letter head for Orchard Noodle Court

```html
<!DOCTYPE html>
<html lang="en">
<head>
<meta charset="utf-8">
<title>Linden Cellular — Business Card</title>
<link rel="stylesheet" href="https://fonts.googleapis.com/css2?family=Montserrat:wght@400;500;700&display=swap">
<style>
  :root {
    --backdrop: #e4e4e4;
    --card: #ffffff;
    --brand-red: #c8151d;
    --deep-red: #8e0b12;
    --ink: #4a4a4a;
    --line-grey: #c9c9c9;
  }
  * { margin: 0; padding: 0; box-sizing: border-box; }
  html, body {
    width: 1200px; height: 901px; overflow: hidden;
    background: var(--backdrop);
    font-family: "Montserrat", Arial, sans-serif;
  }
  .business-card {
    position: absolute; left: 160px; top: 200px;
    width: 880px; height: 500px;
    background: var(--card);
    box-shadow: 0 6px 24px rgba(0,0,0,0.12);
    overflow: hidden;
  }
  .card-waves { position: absolute; inset: 0; }
  .brand {
    position: absolute; left: 70px; top: 196px;
    display: flex; align-items: center; gap: 14px;
  }
  .brand-square {
    width: 36px; height: 36px; background: var(--brand-red);
  }
  .brand-name {
    font-size: 30px; font-weight: 700; color: var(--brand-red);
    letter-spacing: 1px; text-transform: uppercase; line-height: 1;
    white-space: nowrap;
  }
  .contact {
    position: absolute; right: 50px; top: 40px;
    text-align: right;
  }
  .contact-name {
    font-size: 28px; font-weight: 700; color: var(--brand-red);
    text-transform: uppercase; letter-spacing: 1px; line-height: 1.2;
  }
  .contact-title {
    font-size: 16px; font-weight: 500; color: var(--ink);
    margin-top: 2px; margin-bottom: 16px;
  }
  .contact-line {
    display: flex; justify-content: flex-end; align-items: center; gap: 12px;
    font-size: 14px; color: var(--ink); margin-top: 8px; white-space: nowrap;
  }
  .contact-icon { width: 16px; height: 16px; flex: none; }
  .address {
    position: absolute; left: 56px; bottom: 30px;
    color: #ffffff; font-size: 16px; font-weight: 500; line-height: 1.5;
  }
</style>
</head>
<body>
  <main class="business-card">
    <svg class="card-waves" viewBox="0 0 880 500" width="880" height="500" aria-hidden="true">
      <defs>
        <linearGradient id="redBand" x1="0" y1="1" x2="1" y2="0">
          <stop offset="0" stop-color="#8e0b12"/>
          <stop offset="0.5" stop-color="#c8151d"/>
          <stop offset="1" stop-color="#8e0b12"/>
        </linearGradient>
      </defs>
      <path d="M0 398 C 300 384, 600 344, 880 276" fill="none" stroke="#c9c9c9" stroke-width="8"/>
      <path d="M0 422 C 300 408, 600 368, 880 300 L880 500 L0 500 Z" fill="url(#redBand)"/>
      <path d="M0 478 C 300 462, 600 420, 880 350" fill="none" stroke="#e0474d" stroke-width="2" opacity="0.6"/>
    </svg>

    <div class="brand">
      <span class="brand-square"></span>
      <span class="brand-name">Linden Cellular</span>
    </div>

    <section class="contact">
      <h1 class="contact-name">Tobias Krell</h1>
      <p class="contact-title">Operations Manager</p>
      <p class="contact-line">513 555 0142
        <svg class="contact-icon" viewBox="0 0 24 24"><path fill="#c8151d" d="M6.6 10.8a15 15 0 0 0 6.6 6.6l2.2-2.2c.3-.3.7-.4 1-.2 1.1.4 2.3.6 3.6.6.6 0 1 .4 1 1V20c0 .6-.4 1-1 1A17 17 0 0 1 3 4c0-.6.4-1 1-1h3.5c.6 0 1 .4 1 1 0 1.3.2 2.5.6 3.6.1.3 0 .7-.2 1z"/></svg>
      </p>
      <p class="contact-line">513 555 0187
        <svg class="contact-icon" viewBox="0 0 24 24"><rect x="6" y="2" width="12" height="20" rx="2" fill="#c8151d"/><rect x="8" y="5" width="8" height="11" fill="#fff"/></svg>
      </p>
      <p class="contact-line">tobias.krell@lindencellular-mail.com
        <svg class="contact-icon" viewBox="0 0 24 24"><rect x="2" y="5" width="20" height="14" rx="2" fill="#c8151d"/><path d="M3 6l9 7 9-7" fill="none" stroke="#fff" stroke-width="1.6"/></svg>
      </p>
      <p class="contact-line">www.lindencellular-mail.com
        <svg class="contact-icon" viewBox="0 0 24 24"><circle cx="12" cy="12" r="10" fill="#c8151d"/><path d="M2 12h20M12 2c3 3 3 17 0 20M12 2c-3 3-3 17 0 20" fill="none" stroke="#fff" stroke-width="1.3"/></svg>
      </p>
    </section>

    <p class="address">2864 Belmore Ave<br>Cincinnati OH 45219</p>
  </main>
</body>
</html>
```